Branded Flyer Template Libraries Brightwater Lending

Create one-page flyer templates for equipment finance industry to provide a fast turnaround that consistent on-brand for educational and promotional flyers that can be quickly customized with partners logos. These will become a standard toolkit for marketing for use in Adobe Illustrator and editable. customer facing are business owners considering equipment financing typically used for leave behind flyers, email, and handouts. vendor facing to equipment dealers, manufacturers and sales reps who refer customers to us, typically used at trade shows, co branded flyers, and email promotions.
Requesting 1-2 flyer templates with concepts for educational, and promotional.
Brand guide and current flyers in circulation are uploaded as reference.
Look and feel
Each slider illustrates characteristics of the customer's brand and the style your logo design should communicate.

```html
<!DOCTYPE html>
<html lang="en">
<head>
<meta charset="UTF-8">
<title>Brightwater Lending – Equipment Finance Flyer Set</title>
<link href="https://fonts.googleapis.com/css2?family=Outfit:wght@600;700;800&family=Montserrat:wght@400;500;600;700&display=swap" rel="stylesheet">
<style>
  :root{
    --green-dark:#0c4a21;
    --green-light:#8cc163;
    --teal:#7faaa6;
    --pale:#eff5e6;
    --ink:#1f2a22;
    --white:#ffffff;
    --stage:#c6c6c4;
  }
  *{margin:0;padding:0;box-sizing:border-box}
  html,body{width:828px;height:1200px;overflow:hidden;background:var(--stage)}
  .stage{position:relative;width:828px;height:1200px;font-family:"Montserrat",sans-serif;color:var(--ink)}
  .sprites{position:absolute;width:0;height:0;overflow:hidden}

  .flyer{position:absolute;top:324px;width:392px;height:553px;background:var(--white);overflow:hidden;box-shadow:0 3px 10px rgba(0,0,0,.22)}
  .flyer--financing{left:14px}
  .flyer--equipment{left:422px}
  .flyer > *{position:absolute}

  /* header */
  .brand{top:0;left:0;width:100%;height:60px;display:flex;flex-direction:column;align-items:center;justify-content:center;gap:3px}
  .brand-row{display:flex;align-items:center;gap:7px}
  .brand-dot{width:34px;height:34px;border-radius:50%;background:var(--green-dark)}
  .brand-name{font-family:"Outfit",sans-serif;font-weight:600;font-size:14.5px;color:var(--green-dark);letter-spacing:.3px;white-space:nowrap}
  .brand-tag{display:flex;align-items:center;gap:5px;font-size:5px;letter-spacing:2.2px;font-weight:700;color:var(--green-dark);margin-left:40px;margin-top:-14px}
  .brand-tag::before,.brand-tag::after{content:"";width:12px;height:1px;background:var(--green-dark)}

  /* hero */
  .hero-photo{top:60px;left:0;width:392px;height:160px}
  .hero-photo--driver{background:linear-gradient(120deg,#4f4740 0%,#6d6155 30%,#8e8478 55%,#c9ccc8 80%,#e6e8e4 100%)}
  .hero-photo--desk{background:linear-gradient(160deg,#b9b5ae 0%,#e4e2dc 35%,#f3f1ec 55%,#5d5a56 75%,#8c8880 100%)}
  .shapes{top:0;left:0}
  .hero-title{top:213px;left:0;width:100%;text-align:center;font-family:"Outfit",sans-serif;font-weight:800;font-size:24px;line-height:26px;color:var(--white);letter-spacing:.3px;white-space:nowrap}
  .hero-title .accent{color:var(--green-light)}
  .hero-sub{top:269px;left:0;width:100%;text-align:center;color:var(--white);font-size:8.6px;line-height:10px;font-weight:500;white-space:nowrap}

  /* shared section heading */
  .section-title{font-family:"Outfit",sans-serif;font-weight:700;font-size:12px;line-height:14px;color:var(--green-dark);padding-bottom:3px;border-bottom:1.2px solid var(--green-light)}
  .section-title .accent{color:var(--green-light)}

  /* about */
  .about{top:324px;left:35px;width:168px}
  .about .section-title{width:145px;margin-bottom:8px}
  .about p{font-size:6.9px;line-height:9.3px;white-space:nowrap;margin-bottom:9.3px}

  /* benefit list */
  .benefit{top:321px;left:216px;width:160px}
  .benefit .section-title{width:131px;padding-bottom:5px}
  .benefit-list{list-style:none;margin-top:8px}
  .benefit-item{display:flex;align-items:center;gap:10px;height:34.6px}
  .benefit-item svg{flex:none;width:24px;height:24px}
  .benefit-item h3{font-size:7.1px;line-height:9px;font-weight:700;color:var(--green-dark);white-space:nowrap}
  .benefit-item p{font-size:6.8px;line-height:9px;white-space:nowrap}

  /* feature cards */
  .feature-card{top:329px;width:107px;height:72px;border:1px solid var(--green-light);border-radius:4px;background:var(--white);text-align:center}
  .feature-card--one{left:31px}
  .feature-card--two{left:142px}
  .feature-card--three{left:253px}
  .feature-card svg{position:absolute;top:-15px;left:38.5px;width:30px;height:30px}
  .feature-card h3{padding-top:22px;font-size:7.1px;line-height:9px;font-weight:700;color:var(--green-dark);white-space:nowrap}
  .feature-card p{margin-top:4px;font-size:5.8px;line-height:7.1px;white-space:nowrap}

  /* programs band */
  .programs{top:411px;left:0;width:392px;height:83px;background:var(--pale)}
  .programs-title{top:423px;left:35px;font-family:"Outfit",sans-serif;font-weight:700;font-size:10.5px;line-height:12px;color:var(--green-dark);white-space:nowrap;letter-spacing:.2px}
  .programs-title .accent{color:var(--green-light)}
  .programs-text{top:462px;left:35px;font-size:6.9px;line-height:9.3px;white-space:nowrap}
  .programs-rule{top:422px;left:198px;width:1px;height:62px;background:#b9cfa6}
  .programs-list{top:423px;left:211px;list-style:none}
  .programs-list li{position:relative;padding-left:8px;font-size:6.3px;line-height:8.4px;white-space:nowrap;margin-bottom:7.8px}
  .programs-list li::before{content:"";position:absolute;left:0;top:2px;width:4.5px;height:4.5px;border-radius:50%;background:var(--green-light)}

  /* footer */
  .contact{top:507px;left:0;width:100%;text-align:center}
  .contact h2{font-family:"Outfit",sans-serif;font-weight:700;font-size:11.5px;line-height:14px;color:var(--green-dark)}
  .contact-line{display:flex;justify-content:center;align-items:center;gap:4px;font-size:7.2px;line-height:10px;margin-top:1px;white-space:nowrap}
  .contact-line .dot{display:inline-block;width:5.5px;height:5.5px;border-radius:50%;background:var(--green-light);margin-right:3px;vertical-align:0}
  .bottom-bar{top:549px;left:36px;width:320px;height:4px;background:var(--green-light)}
</style>
</head>
<body>
<div class="stage">
  <svg class="sprites" aria-hidden="true">
    <symbol id="coin" viewBox="0 0 24 24">
      <circle cx="12" cy="12" r="12" fill="#8cc163"/>
      <circle cx="12" cy="12" r="7.5" fill="none" stroke="#fff" stroke-width="1.2"/>
      <text x="12" y="15.3" text-anchor="middle" font-family="Montserrat,sans-serif" font-size="9" font-weight="700" fill="#fff">$</text>
    </symbol>
  </svg>

  <!-- Educational flyer -->
  <article class="flyer flyer--financing">
    <div class="hero-photo hero-photo--driver" role="img" aria-label="Photo of a smiling delivery driver at the wheel of a work van"></div>
    <svg class="shapes" width="392" height="553" viewBox="0 0 392 553">
      <rect x="206" y="290" width="186" height="204" fill="var(--pale)"/>
      <path d="M160 298 Q300 280 392 318 L392 340 Q300 298 160 298 Z" fill="var(--teal)"/>
      <path d="M0 158 Q196 234 392 158 L392 172 Q196 238 0 174 Z" fill="var(--green-light)"/>
      <path d="M0 173 Q196 237 392 171 L392 325 Q196 266 0 323 Z" fill="var(--green-dark)"/>
    </svg>

    <header class="brand">
      <div class="brand-row"><span class="brand-dot"></span><span class="brand-name">BRIGHTWATER LENDING</span></div>
      <div class="brand-tag">EQUIPMENT FINANCE</div>
    </header>

    <h1 class="hero-title">EQUIPMENT FINANCING<br><span class="accent">MADE SIMPLE</span></h1>
    <p class="hero-sub">Get the equipment you need while preserving cash flow.</p>

    <section class="about">
      <h2 class="section-title"><span class="accent">About</span> Us</h2>
      <p>Lorem ipsum dolor sit amet, consectetur<br>adipiscing elit, sed do eiusmod tempor<br>incididunt ut labore et dolore magna aliqua.<br>Ut enim ad minim veniam, quis nostrud<br>exercitation ullamco laboris nisi ut aliquip<br>ex ea commodo consequat.</p>
      <p>Duis aute irure dolor in reprehenderit in<br>voluptate velit esse cillum dolore eu fugiat<br>nulla pariatur. Excepteur sint occaecat<br>cupidatat non proident, sunt in culpa qui<br>officia deserunt mollit anim id est laborum.<br>Lorem ipsum dolor sit amet, consectetur<br>adipiscing elit</p>
    </section>

    <section class="benefit">
      <h2 class="section-title">Benefit</h2>
      <ul class="benefit-list">
        <li class="benefit-item"><svg viewBox="0 0 24 24"><use href="#coin"/></svg><div><h3>Preserve Cash Flow</h3><p>Lorem ipsum dolor sit amet,<br>consectetur adipiscing elit,</p></div></li>
        <li class="benefit-item"><svg viewBox="0 0 24 24"><use href="#coin"/></svg><div><h3>Preserve Cash Flow</h3><p>Lorem ipsum dolor sit amet,<br>consectetur adipiscing elit,</p></div></li>
        <li class="benefit-item"><svg viewBox="0 0 24 24"><use href="#coin"/></svg><div><h3>Preserve Cash Flow</h3><p>Lorem ipsum dolor sit amet,<br>consectetur adipiscing elit,</p></div></li>
        <li class="benefit-item"><svg viewBox="0 0 24 24"><use href="#coin"/></svg><div><h3>Preserve Cash Flow</h3><p>Lorem ipsum dolor sit amet,<br>consectetur adipiscing elit,</p></div></li>
      </ul>
    </section>

    <footer class="contact">
      <h2>Talk to a Financing Specialist Today</h2>
      <div class="contact-line">
        <span><span class="dot"></span>brightwaterlending.com</span><span>|</span>
        <span><span class="dot"></span>hello@brightwaterlending.com</span><span>|</span>
        <span><span class="dot"></span>(800) 555-0148</span>
      </div>
    </footer>
    <div class="bottom-bar"></div>
  </article>

  <!-- Promotional flyer -->
  <article class="flyer flyer--equipment">
    <div class="hero-photo hero-photo--desk" role="img" aria-label="Photo of a hand writing on financial papers beside a calculator on a desk"></div>
    <svg class="shapes" width="392" height="553" viewBox="0 0 392 553">
      <path d="M160 298 Q300 280 392 318 L392 340 Q300 298 160 298 Z" fill="var(--teal)"/>
      <path d="M0 158 Q196 234 392 158 L392 172 Q196 238 0 174 Z" fill="var(--green-light)"/>
      <path d="M0 173 Q196 237 392 171 L392 325 Q196 266 0 323 Z" fill="var(--green-dark)"/>
    </svg>

    <header class="brand">
      <div class="brand-row"><span class="brand-dot"></span><span class="brand-name">BRIGHTWATER LENDING</span></div>
      <div class="brand-tag">EQUIPMENT FINANCE</div>
    </header>

    <h1 class="hero-title">GET THE EQUIPMENT<br>YOU NEED <span class="accent">TODAY</span></h1>
    <p class="hero-sub">Flexible financing solutions designed for your business succes.</p>

    <div class="feature-card feature-card--one"><svg viewBox="0 0 24 24"><use href="#coin"/></svg><h3>Preserve Cash Flow</h3><p>Lorem ipsum dolor sit amet,<br>consectetur adipiscing elit,<br>sed do eiusmod tempor<br>incididunt ut labore et dolore</p></div>
    <div class="feature-card feature-card--two"><svg viewBox="0 0 24 24"><use href="#coin"/></svg><h3>Preserve Cash Flow</h3><p>Lorem ipsum dolor sit amet,<br>consectetur adipiscing elit,<br>sed do eiusmod tempor<br>incididunt ut labore et dolore</p></div>
    <div class="feature-card feature-card--three"><svg viewBox="0 0 24 24"><use href="#coin"/></svg><h3>Preserve Cash Flow</h3><p>Lorem ipsum dolor sit amet,<br>consectetur adipiscing elit,<br>sed do eiusmod tempor<br>incididunt ut labore et dolore</p></div>

    <div class="programs"></div>
    <h2 class="programs-title">SPECIAL FINANCING<br>PROGRAMS FOR <span class="accent">QUALIFIED<br>BUSINESSES</span></h2>
    <p class="programs-text">Lorem ipsum dolor sit amet, consectetur<br>dipiscing elit, sed do eiusmod tempor .</p>
    <div class="programs-rule"></div>
    <ul class="programs-list">
      <li>Lorem ipsum dolor sit amet, consectetur<br>adipiscing elit, sed do eiusmod tempor<br>Incididunt ut labore et dolore magna aliqua.</li>
      <li>Lorem ipsum dolor sit amet, consectetur<br>adipiscing elit, sed do eiusmod tempor<br>Incididunt ut labore et dolore magna aliqua.</li>
    </ul>

    <footer class="contact">
      <h2>Talk to a Financing Specialist Today</h2>
      <div class="contact-line">
        <span><span class="dot"></span>brightwaterlending.com</span><span>|</span>
        <span><span class="dot"></span>hello@brightwaterlending.com</span><span>|</span>
        <span><span class="dot"></span>(800) 555-0148</span>
      </div>
    </footer>
    <div class="bottom-bar"></div>
  </article>
</div>
</body>
</html>
```